Poetry Book Cover Design Project

Looking for a minimalistic book cover design for a collection of poems. The book title is "Where The Lanterns Drift Slowly Apart". There are three parts to the book. First covers poetry in the theme of Rage. Second love and desire. The third is strange poems. Essentially the sections are "Rage", "Desire" and the "Strange". The reason for the title "Where The Lanterns Drift Slowly Apart" is as if someone is writing these till life changes towards the intended outcome as felt in each poem. I want to have the author's name "Nuwanthi Karunasekera" at the bottom. Ilustration attached.
- Minimalistic

```html
<!DOCTYPE html>
<html lang="en">
<head>
<meta charset="utf-8">
<title>Where The Lanterns Drift Slowly Apart — Book Cover</title>
<link href="https://fonts.googleapis.com/css2?family=Cinzel:wght@400;500&display=swap" rel="stylesheet">
<style>
  :root {
    --page-bg: #e6e6e6;
    --cover-red: #841f27;
    --ink-light: #fbf4f0;
    --crowd-deep: #8e161c;
    --crowd-mid: #b01e26;
    --crowd-bright: #d0343a;
    --crowd-glow: #dc5a52;
  }
  * { margin: 0; padding: 0; box-sizing: border-box; }
  html, body {
    width: 1200px;
    height: 999px;
    overflow: hidden;
    background: var(--page-bg);
  }
  .cover {
    position: absolute;
    left: 280px;
    top: 20px;
    width: 640px;
    height: 960px;
    background: var(--cover-red);
    color: var(--ink-light);
    font-family: "Cinzel", serif;
    text-align: center;
  }
  .title { font-weight: 400; }
  .title-lead {
    position: absolute;
    top: 34px;
    left: 0;
    width: 100%;
    font-size: 36px;
    font-weight: 400;
    letter-spacing: 0.5px;
    line-height: 1;
  }
  .title-key {
    position: absolute;
    top: 80px;
    left: 0;
    width: 100%;
    display: flex;
    align-items: center;
    gap: 16px;
    font-size: 96px;
    font-weight: 400;
    line-height: 1;
  }
  .title-key .rule {
    flex: 1;
    height: 2px;
    background: var(--ink-light);
  }
  .title-tail {
    position: absolute;
    top: 182px;
    left: 0;
    width: 100%;
    font-size: 70px;
    font-weight: 400;
    line-height: 1;
  }
  .illustration {
    position: absolute;
    top: 270px;
    left: 0;
    width: 640px;
    height: 620px;
  }
  .author {
    position: absolute;
    top: 906px;
    left: 0;
    width: 100%;
    font-size: 34px;
    font-weight: 400;
    line-height: 1;
  }
</style>
</head>
<body>
  <main class="cover">
    <h1 class="title">
      <span class="title-lead">WHERE THE LANTERNS DRIFT</span>
      <span class="title-key"><span class="rule"></span>SLOWLY<span class="rule"></span></span>
      <span class="title-tail">APART</span>
    </h1>
    <svg class="illustration" viewBox="0 0 640 620" role="img" aria-label="Illustration for a poetry collection in three parts, Rage, Desire and Strange: rows of identical red-hooded figures with hands joined, and one figure near the centre pulling back his hood and looking upward, standing apart from the crowd">
      <defs>
        <linearGradient id="crowd-tone" x1="0" y1="0" x2="0" y2="1">
          <stop offset="0" stop-color="var(--cover-red)"/>
          <stop offset="0.07" stop-color="var(--crowd-deep)"/>
          <stop offset="0.5" stop-color="var(--crowd-mid)"/>
          <stop offset="0.93" stop-color="var(--crowd-deep)"/>
          <stop offset="1" stop-color="var(--cover-red)"/>
        </linearGradient>
        <radialGradient id="lone-figure-glow" cx="0.5" cy="0.6" r="0.45">
          <stop offset="0" stop-color="var(--crowd-glow)" stop-opacity="0.85"/>
          <stop offset="0.45" stop-color="var(--crowd-bright)" stop-opacity="0.5"/>
          <stop offset="1" stop-color="var(--crowd-bright)" stop-opacity="0"/>
        </radialGradient>
      </defs>
      <rect class="crowd-field" width="640" height="620" fill="url(#crowd-tone)"/>
      <rect class="lone-figure-light" width="640" height="620" fill="url(#lone-figure-glow)"/>
    </svg>
    <p class="author">Nuwanthi Karunasekera</p>
  </main>
</body>
</html>
```